Velmora Care Collective Presentation Folder, for Cancer Awareness, VERY COLORFUL AND MODERN

Presentation Folder I know pretty much what i want so it should be very eazy , I have included files from folders I use now rebrand them to my new company they will be fine, no sense re creating the wheel
Full Bleed Size
20.87" x 16.68"
53 x 42.4 cm
6260 x 5004 pixels
Document Trim Size
20.75" x 16.56"
52.7 x 42.1 cm
6225 x 4969 pixels

Industry/Entity Type

Medical

Font styles to use
Serif

Colors

Designer to choose colors to be used in the design.

Requirements
Must have
• really I am not looking for some one to redesign, we like our folder front page and would like to see new word information added., there are two folder front pages to choose from
• So Keep the original front page and redesign the back page and the pockets
• Can Make your Design off of one of the ones I already uploaded
Nice to have
• Keep the same color schemes, Keep the original front page and redesign the back page and the pockets
Should not have
• DO not recreate the front covers, use what I gave you and just rebrand

```html
<!DOCTYPE html>
<html lang="en">
<head>
<meta charset="utf-8">
<title>Velmora Care Collective — Hereditary Cancer Screening Folder</title>
<link rel="stylesheet" href="https://fonts.googleapis.com/css2?family=Cinzel:wght@400;500&family=Raleway:wght@400;600;700;800&display=swap">
<style>
  :root {
    --stage: #333333;
    --paper: #ffffff;
    --green: #8cc63f;
    --navy: #1a1f56;
    --ink: #1d2148;
    --photo-grey-sky: #e8e8e8;
    --photo-grey-sand: #c9c9c9;
    --photo-grey-shadow: #8d8d8d;
    --photo-teal-light: #dfe8ea;
    --photo-teal-mid: #9fb6ba;
    --photo-teal-dark: #5a7a80;
  }
  * { box-sizing: border-box; margin: 0; padding: 0; }
  html, body { width: 1200px; height: 1078px; overflow: hidden; }
  body { background: var(--stage); font-family: "Raleway", sans-serif; position: relative; }

  .folder { position: absolute; left: 35px; top: 89px; width: 1130px; height: 900px; display: flex; }
  .panel { position: relative; width: 565px; height: 900px; background: var(--paper); overflow: hidden; }

  .band-green { position: absolute; left: 0; right: 0; top: 66px; height: 58px; background: var(--green); }
  .band-navy { position: absolute; left: 0; right: 0; top: 770px; height: 58px; background: var(--navy); }

  /* back panel */
  .back-photo { position: absolute; left: 28px; top: 186px; width: 509px; height: 404px;
    background: linear-gradient(180deg, var(--photo-grey-sky) 0%, #f6f6f6 48%, var(--photo-grey-sand) 70%, var(--photo-grey-shadow) 100%); }
  .back-intro { position: absolute; left: 24px; right: 24px; top: 604px; font-size: 10px; line-height: 1.4; color: var(--ink); text-align: center; }
  .back-intro strong { font-weight: 700; }
  .back-tagline { position: absolute; left: 10px; right: 10px; top: 662px; font-size: 12.5px; font-weight: 800; line-height: 1.5; color: var(--ink); text-align: center; letter-spacing: -0.2px; }
  .back-tagline span { display: block; white-space: nowrap; }
  .brand { position: absolute; left: 0; right: 0; top: 724px; display: flex; align-items: center; justify-content: center; gap: 10px; }
  .brand-mark { width: 26px; height: 26px; border-radius: 50%; background: var(--navy); }
  .brand-name { font-family: "Raleway", sans-serif; font-weight: 700; font-size: 15px; color: var(--navy); letter-spacing: .5px; }

  /* front panel */
  .front-title { position: absolute; left: 0; right: 18px; top: 66px; height: 58px; line-height: 58px; text-align: right;
    font-family: "Cinzel", serif; font-weight: 400; font-size: 29px; color: var(--paper); letter-spacing: .5px; }
  .front-banner { position: absolute; right: 40px; top: 133px; width: 392px; height: 48px; background: var(--navy);
    font-family: "Cinzel", serif; font-size: 13px; color: var(--green); line-height: 48px; text-align: center; white-space: nowrap; }
  .ribbon { position: absolute; right: 14px; top: 140px; width: 20px; height: 44px; border-radius: 10px 10px 2px 2px;
    background: linear-gradient(135deg, #d88ac9, #6fc3ec); }
  .front-lede { position: absolute; right: 58px; top: 190px; width: 360px; font-size: 10.5px; line-height: 1.35; color: var(--ink); text-align: center; }
  .front-photo { position: absolute; left: 0; right: 0; top: 240px; height: 520px;
    background: linear-gradient(160deg, var(--photo-teal-light) 0%, var(--photo-teal-mid) 45%, var(--photo-teal-dark) 100%); }
  .front-seal { position: absolute; left: 70px; top: 755px; width: 88px; height: 88px; border-radius: 50%; background: var(--paper); border: 4px solid var(--navy); }
  .front-strap { position: absolute; left: 180px; right: 20px; top: 770px; height: 58px; line-height: 58px;
    font-size: 15px; font-weight: 700; color: var(--paper); letter-spacing: 1px; text-transform: uppercase; white-space: nowrap; }
</style>
</head>
<body>
  <main class="folder">
    <section class="panel panel-back">
      <div class="band-green"></div>
      <div class="back-photo" role="img" aria-label="Black and white photo of a multi-generation family walking hand in hand on a beach"></div>
      <p class="back-intro"><strong>Hereditary cancer screening</strong> provides vital information to help people with a strong personal or family history of cancer understand their own risk of developing the disease. With this information, they can take steps to Potentially Prevent Cancer, Delay the Onset of Cancer or Catch it at an Earlier stage when outcomes and survival rates are Better.</p>
      <p class="back-tagline"><span>Don't be Afraid of the Answer: Knowledge is Power and Power Eradicates Fear.</span><span>When You are Fearless, You Will Make all the Right Choices!</span></p>
      <div class="brand"><span class="brand-mark"></span><span class="brand-name">Velmora Care Collective</span></div>
      <div class="band-navy"></div>
    </section>

    <section class="panel panel-front">
      <div class="band-green"></div>
      <h1 class="front-title">Hereditary Cancer Screening</h1>
      <div class="front-banner">Doctors are the gatekeepers to genetic testing</div>
      <div class="ribbon" role="img" aria-label="Cancer awareness ribbon"></div>
      <p class="front-lede">We have an obligation to help patients understand genetic risk and how testing can guide heath care decisions</p>
      <div class="front-photo" role="img" aria-label="Teal-toned photo of a family sharing a meal at an outdoor table"></div>
      <div class="band-navy"></div>
      <div class="front-seal" aria-hidden="true"></div>
      <p class="front-strap">The test you order for your patients</p>
    </section>
  </main>
</body>
</html>
```